Bref créative
business card for vegan prepared foods company
ZELO, taste the bright side
Simple
Petra Valdoni
Chef/Owner
www.zelofoods.example
zelofoods@mailbox.example
I would my business card to have on one side logo+web address, on the other side logo+ the rest of the info
logo and website address

```html
<!DOCTYPE html>
<html lang="en">
<head>
<meta charset="utf-8">
<title>Zelo business cards</title>
<link href="https://fonts.googleapis.com/css2?family=Comfortaa:wght@300;400;700&display=swap" rel="stylesheet">
<style>
  :root {
    --bg: #2b2c2b;
    --card-dark: #1f4129;
    --card-dark-2: #2a5633;
    --band-green: #3cb44a;
    --band-green-2: #55c95a;
    --leaf: #4fbf4f;
    --text-light: #c9e8b8;
    --text-green: #6ccf5a;
    --text-on-band: #1d4a25;
  }
  * { margin: 0; padding: 0; box-sizing: border-box; }
  html, body { width: 1200px; height: 698px; overflow: hidden; }
  body {
    background: var(--bg);
    font-family: "Comfortaa", sans-serif;
    position: relative;
  }
  .card {
    position: absolute;
    top: 194px;
    width: 540px;
    height: 310px;
    border-radius: 18px;
    overflow: hidden;
    background: linear-gradient(160deg, var(--card-dark-2), var(--card-dark));
  }
  .card--front { left: 40px; }
  .card--back { left: 620px; }

  .front-band {
    position: absolute;
    inset: 0 0 auto 0;
    height: 118px;
    background: linear-gradient(90deg, var(--band-green), var(--band-green-2));
  }
  .website {
    position: absolute;
    left: 34px;
    top: 44px;
    font-size: 26px;
    letter-spacing: 5px;
    color: var(--text-on-band);
    font-weight: 700;
  }

  .brand {
    position: absolute;
    display: flex;
    align-items: center;
    gap: 16px;
  }
  .brand-name {
    font-size: 64px;
    font-weight: 700;
    letter-spacing: 6px;
    color: var(--text-green);
    line-height: 1;
  }
  .brand-dot {
    width: 58px;
    height: 58px;
    border-radius: 50%;
    background: var(--leaf);
  }
  .tagline {
    position: absolute;
    font-size: 17px;
    color: var(--text-green);
    font-weight: 300;
    letter-spacing: 1px;
  }
  .card--front .brand { left: 120px; top: 150px; }
  .card--front .tagline { left: 124px; top: 228px; }

  .card--back .brand { left: 120px; top: 60px; }
  .card--back .tagline { left: 124px; top: 138px; }

  .contact {
    position: absolute;
    left: 40px;
    top: 196px;
    color: var(--text-light);
  }
  .person-name { font-size: 17px; color: var(--text-green); font-weight: 400; }
  .person-role { font-size: 11px; margin: 3px 0 8px; }
  .contact-line {
    display: flex;
    align-items: center;
    gap: 7px;
    font-size: 11px;
    margin-top: 4px;
  }
  .contact-line svg { width: 11px; height: 11px; fill: var(--text-green); }
</style>
</head>
<body>
  <section class="card card--front" aria-label="Card front">
    <div class="front-band">
      <p class="website">www.zelofoods.example</p>
    </div>
    <div class="brand">
      <span class="brand-name">ZELO</span>
      <span class="brand-dot"></span>
    </div>
    <p class="tagline">taste the bright side</p>
  </section>

  <section class="card card--back" aria-label="Card back">
    <div class="brand">
      <span class="brand-name">ZELO</span>
      <span class="brand-dot"></span>
    </div>
    <p class="tagline">taste the bright side</p>
    <div class="contact">
      <p class="person-name">Petra Valdoni</p>
      <p class="person-role">Chef/Owner</p>
      <p class="contact-line">
        <svg viewBox="0 0 12 12"><path d="M3 1h2l1 3-1.5 1a6 6 0 0 0 2.5 2.5L8 6l3 1v2c0 1-1 2-2 2A8 8 0 0 1 1 3c0-1 1-2 2-2z"/></svg>
        555 270 0142
      </p>
      <p class="contact-line">
        <svg viewBox="0 0 12 12"><rect x="3" y="0.5" width="6" height="11" rx="1.2"/></svg>
        555 282 0199
      </p>
      <p class="contact-line">
        <svg viewBox="0 0 12 12"><path d="M1 2.5h10v7H1z M1 2.5l5 4 5-4" fill="none" stroke="#6ccf5a" stroke-width="1.2"/></svg>
        zelofoods@mailbox.example
      </p>
    </div>
  </section>
</body>
</html>
```